Design for online reviews widget

Attached is a wireframe of a widget we need designing to display reviews on websites from multiple sources. We need this provided at 3 different sizes including full screen, contained (like the wireframe) and mobile.
You have completely free rein on the styling.
The only elements that should remain untouched are the blue stars (https://www.filevault-demo.net/s/8pwtmz2lq4nv90h/kt%20stars.ai?dl=0) and powered by logo at the bottom.
Ignore the menu at the top of the wireframe, this is just from the website the widget will be placed on.
Target Market(s)
Businesses
Look and feel
Each slider illustrates characteristics of the customer's brand and the style your logo design should communicate.

```html
<!DOCTYPE html>
<html lang="en">
<head>
<meta charset="utf-8">
<title>Reviews Widget</title>
<link rel="stylesheet" href="https://fonts.googleapis.com/css2?family=Montserrat:wght@400;500;600;700&family=Roboto:wght@400;500&display=swap">
<style>
  :root {
    --page: #ffffff;
    --band: #f4f4f4;
    --card: #ffffff;
    --ink: #333333;
    --ink-soft: #555555;
    --star-blue: #3fb8ec;
    --gold: #f5b41c;
    --accent: #3ded82;
    --accent-text: #2fe07a;
    --nav-circle: #e9e9e9;
    --nav-chevron: #c4c4c4;
    --score-blue: #0d4f99;
    --border: #333333;
  }
  * { box-sizing: border-box; margin: 0; padding: 0; }
  html, body { width: 1200px; height: 1000px; overflow: hidden; background: var(--page); }
  body { position: relative; font-family: "Montserrat", sans-serif; color: var(--ink); }

  .reviews-widget { position: absolute; left: 0; top: 171px; width: 1200px; height: 657px; background: var(--band); }

  .summary { position: absolute; left: 111px; top: 26px; }
  .summary__label { font-size: 15.5px; font-weight: 500; color: var(--ink); }
  .summary__stars { display: flex; gap: 7px; margin-top: 12px; }
  .summary__stars svg { width: 33px; height: 33px; }

  .filter { position: absolute; right: 112px; top: 33px; width: 183px; height: 51px; border: 1px solid var(--border); border-radius: 5px; display: flex; background: var(--card); }
  .filter__label { flex: 1; display: flex; align-items: center; justify-content: center; font-family: "Roboto", sans-serif; font-size: 16px; color: var(--ink); border-right: 1px solid var(--border); }
  .filter__toggle { width: 42px; display: flex; align-items: center; justify-content: center; }

  .carousel__arrow { position: absolute; top: 276px; width: 106px; height: 106px; border-radius: 50%; background: var(--nav-circle); display: flex; align-items: center; justify-content: center; }
  .carousel__arrow--prev { left: 58px; }
  .carousel__arrow--next { left: 1035px; }

  .review-card { position: absolute; top: 122px; width: 467px; height: 429px; background: var(--card); border-radius: 18px; box-shadow: 0 2px 6px rgba(0,0,0,0.08); padding: 28px 44px 0 44px; }
  .review-card--left { left: 111px; }
  .review-card--right { left: 621px; }
  .review-card__head { display: flex; justify-content: space-between; align-items: center; height: 48px; }
  .source-name { display: flex; align-items: center; gap: 7px; font-size: 16px; font-weight: 700; color: var(--ink); }
  .source-name__dot { width: 14px; height: 14px; border-radius: 50%; background: var(--ink); }
  .score-badge { width: 44px; height: 44px; border-radius: 50%; background: var(--score-blue); border: 3px solid #fff; box-shadow: 0 0 0 2px var(--score-blue); margin-right: 3px; }
  .gold-stars { display: flex; gap: 2px; margin-right: 18px; }
  .gold-stars svg { width 27px; width: 27px; height: 27px; }
  .review-card__title { margin-top: 12px; font-size: 21px; font-weight: 600; line-height: 28px; color: var(--ink); }
  .review-card__body { margin-top: 12px; font-size: 14px; line-height: 20.6px; color: var(--ink-soft); }
  .review-card__meta { margin-top: 14px; font-size: 14px; line-height: 20.6px; color: var(--ink); }
  .review-card__meta b { font-weight: 600; }
  .ratings { display: grid; grid-template-columns: 133px auto; }
  .review-card__footer { position: absolute; right: 44px; bottom: 34px; font-size: 12.5px; font-weight: 500; color: var(--accent-text); }

  .load-more { position: absolute; left: 111px; top: 582px; width: 184px; height: 52px; border-radius: 26px; background: var(--accent); color: #fff; font-size: 16px; font-weight: 600; display: flex; align-items: center; justify-content: center; }

  .powered-by { position: absolute; right: 128px; top: 576px; text-align: right; }
  .powered-by__label { font-family: "Roboto", sans-serif; font-size: 13.5px; color: var(--ink); margin-right: 43px; }
  .powered-by__brand { display: flex; align-items: center; gap: 8px; margin-top: 6px; font-size: 20px; font-weight: 700; color: var(--ink); }
  .powered-by__mark { width: 30px; height: 30px; border-radius: 50%; background: var(--star-blue); }
</style>
</head>
<body>
<section class="reviews-widget" aria-label="Customer reviews">
  <div class="summary">
    <p class="summary__label">Combined Review Score 4.3 out of 5</p>
    <div class="summary__stars" aria-label="4.3 out of 5 stars">
      <svg viewBox="0 0 32 32"><circle cx="16" cy="16" r="16" fill="var(--star-blue)"/><path d="M16 5.5l3.1 6.6 7.2.8-5.4 4.9 1.5 7.1L16 21.3l-6.4 3.6 1.5-7.1-5.4-4.9 7.2-.8z" fill="#fff"/></svg>
      <svg viewBox="0 0 32 32"><circle cx="16" cy="16" r="16" fill="var(--star-blue)"/><path d="M16 5.5l3.1 6.6 7.2.8-5.4 4.9 1.5 7.1L16 21.3l-6.4 3.6 1.5-7.1-5.4-4.9 7.2-.8z" fill="#fff"/></svg>
      <svg viewBox="0 0 32 32"><circle cx="16" cy="16" r="16" fill="var(--star-blue)"/><path d="M16 5.5l3.1 6.6 7.2.8-5.4 4.9 1.5 7.1L16 21.3l-6.4 3.6 1.5-7.1-5.4-4.9 7.2-.8z" fill="#fff"/></svg>
      <svg viewBox="0 0 32 32"><circle cx="16" cy="16" r="16" fill="var(--star-blue)"/><path d="M16 5.5l3.1 6.6 7.2.8-5.4 4.9 1.5 7.1L16 21.3l-6.4 3.6 1.5-7.1-5.4-4.9 7.2-.8z" fill="#fff"/></svg>
      <svg viewBox="0 0 32 32"><circle cx="16" cy="16" r="16" fill="var(--star-blue)"/><path d="M16 5.5l3.1 6.6 7.2.8-5.4 4.9 1.5 7.1L16 21.3l-6.4 3.6 1.5-7.1-5.4-4.9 7.2-.8z" fill="#fff"/></svg>
    </div>
  </div>

  <div class="filter">
    <span class="filter__label">Filter results</span>
    <span class="filter__toggle"><svg width="16" height="10" viewBox="0 0 16 10"><path d="M0 0h16L8 9z" fill="var(--ink)"/></svg></span>
  </div>

  <div class="carousel__arrow carousel__arrow--prev" aria-label="Previous">
    <svg width="30" height="46" viewBox="0 0 30 46"><path d="M26 3L6 23l20 20" fill="none" stroke="var(--nav-chevron)" stroke-width="4"/></svg>
  </div>

  <article class="review-card review-card--left">
    <div class="review-card__head">
      <span class="source-name"><span class="source-name__dot"></span>TradeVouch</span>
      <span class="score-badge" aria-label="Score badge"></span>
    </div>
    <h2 class="review-card__title">Front door with windows each side and side window</h2>
    <p class="review-card__body">This is the second time we have used harbourline home Improvements , and the service is amazing! Owen came round several times as we keep changing our minds and he was so helpful and gave us good advice, and the guys who do the fitting are efficient and tidy . I've got to say the end result is amazing and I have recommended to many of friends . Thanks Harbourline</p>
    <div class="review-card__meta ratings">
      <span><b>Reliablity:</b> 9.38</span><span><b>Courtesy:</b> 10</span>
      <span><b>Tidiness:</b> 9.84</span><span><b>Workmanship:</b> 10</span>
    </div>
    <p class="review-card__footer">Verified 28th September 2021 | Located in Millbrook</p>
  </article>

  <article class="review-card review-card--right">
    <div class="review-card__head">
      <span class="source-name"><span class="source-name__dot"></span>Searchly</span>
      <span class="gold-stars" aria-label="5 stars">
        <svg viewBox="0 0 24 24"><path d="M12 1.5l3.2 6.9 7.3.8-5.5 5 1.6 7.3L12 17.8l-6.6 3.7L7 14.2l-5.5-5 7.3-.8z" fill="var(--gold)"/></svg>
        <svg viewBox="0 0 24 24"><path d="M12 1.5l3.2 6.9 7.3.8-5.5 5 1.6 7.3L12 17.8l-6.6 3.7L7 14.2l-5.5-5 7.3-.8z" fill="var(--gold)"/></svg>
        <svg viewBox="0 0 24 24"><path d="M12 1.5l3.2 6.9 7.3.8-5.5 5 1.6 7.3L12 17.8l-6.6 3.7L7 14.2l-5.5-5 7.3-.8z" fill="var(--gold)"/></svg>
        <svg viewBox="0 0 24 24"><path d="M12 1.5l3.2 6.9 7.3.8-5.5 5 1.6 7.3L12 17.8l-6.6 3.7L7 14.2l-5.5-5 7.3-.8z" fill="var(--gold)"/></svg>
        <svg viewBox="0 0 24 24"><path d="M12 1.5l3.2 6.9 7.3.8-5.5 5 1.6 7.3L12 17.8l-6.6 3.7L7 14.2l-5.5-5 7.3-.8z" fill="var(--gold)"/></svg>
      </span>
    </div>
    <h2 class="review-card__title">Positive: Professionalism, Quality, Value</h2>
    <p class="review-card__body">The team did a good job of replacing a large feature window spanning two floors, as well as the others in my property. They're a professional group who were willing to work out solutions to any problem, especially compared to other companies. Prices are fair, and my new UPVC windows look great. Special thanks to Marcus for being so accommodating and for the good communication throughout.</p>
    <p class="review-card__meta"><b>Service:</b> Window installation</p>
    <p class="review-card__footer">11 months ago by Daniel Roake</p>
  </article>

  <div class="carousel__arrow carousel__arrow--next" aria-label="Next">
    <svg width="30" height="46" viewBox="0 0 30 46"><path d="M4 3l20 20L4 43" fill="none" stroke="var(--nav-chevron)" stroke-width="4"/></svg>
  </div>

  <div class="load-more">Load more</div>

  <div class="powered-by">
    <p class="powered-by__label">Powered by</p>
    <p class="powered-by__brand"><span class="powered-by__mark"></span>ReviewMesh</p>
  </div>
</section>
</body>
</html>
```